skin elixir serum with snail extract

I am working at a natural skincare company. We are going to launch a new product - a skin serum. completely natural, super concentrated, multi use (face, neck , eyes). But we need the packaging (box and bottle label) to be aligned to our brand's philosophy, design etc. (See more at dovrenta.com)

Here's a more detailed description :
"Elevate your skincare routine with BrimZest Tonic, the ultimate one-drop wonder enriched with potent snail secretion. Experience the magic as our 100% natural serum transforms your face, eyes, décolleté, and neck. Get ready to say Wow to a new level of radiance!"

Target Market(s)

natural skincare enthusiasts - beauty pioneers

Industry/Entity Type

beauty - wellness

Requirements
Nice to have
• based on the overall brand philosophy (see dovrenta.com)

```html
<!DOCTYPE html>
<html lang="en">
<head>
<meta charset="utf-8">
<title>Dovrenta Skin Elixir Serum – Box and Label Dieline</title>
<link rel="stylesheet" href="https://fonts.googleapis.com/css2?family=Poppins:wght@400;500;600&display=swap">
<style>
  :root {
    --backdrop: #333333;
    --terracotta: #cf8664;
    --sand: #ecdab3;
    --paper: #ffffff;
    --ink: #333333;
    --on-terracotta: #ffffff;
  }
  * { margin: 0; padding: 0; box-sizing: border-box; }
  html, body { width: 1200px; height: 903px; overflow: hidden; background: var(--backdrop); }
  .canvas { position: relative; width: 1200px; height: 903px; font-family: "Poppins", sans-serif; }
  .dieline { position: absolute; left: 0; top: 0; }
  .abs { position: absolute; }
  .center { text-align: center; color: var(--on-terracotta); }

  .brand { font-weight: 500; font-size: 22px; line-height: 28px; letter-spacing: 0.5px; }

  .copy { color: var(--ink); font-size: 8.6px; line-height: 12px; width: 124px; }
  .copy .strong { font-weight: 600; }
  .copy .gap-1 { margin-top: 10px; }
  .copy .gap-2 { margin-top: 17px; }
  .copy .gap-3 { margin-top: 22px; }
  .copy .gap-4 { margin-top: 15px; }

  .product-name { font-size: 10.5px; line-height: 15px; letter-spacing: 0.2px; }
  .uses { font-size: 7.5px; line-height: 10px; letter-spacing: 0.5px; }
  .claims { font-size: 6.6px; line-height: 10px; }
  .volume { font-size: 6.6px; line-height: 11px; }
  .volume b { font-weight: 600; }

  .label .brand { font-size: 15px; line-height: 20px; }
  .label .product-name { font-size: 8.5px; line-height: 12px; }
  .label .uses { font-size: 5.6px; line-height: 8px; }
  .label .claims { font-size: 5px; line-height: 8px; }
  .label .volume { font-size: 5px; line-height: 8px; }
</style>
</head>
<body>
<main class="canvas">
  <svg class="dieline" width="1200" height="903" viewBox="0 0 1200 903">
    <polygon class="side-panel" role="img" aria-label="Sand paisley and lattice pattern on left side panel and flaps"
      fill="var(--sand)" points="264,172 383,172 383,740 264,740 264,647 240,647 196,627 196,285 240,265 264,265"/>
    <polygon class="side-panel" role="img" aria-label="Sand paisley and lattice pattern on right side panel and flaps"
      fill="var(--sand)" points="538,172 658,172 658,262 682,285 682,627 658,650 658,740 538,740"/>
    <path class="front-panel" role="img" aria-label="Terracotta panel with faint tonal pattern"
      fill="var(--terracotta)" d="M385,90 Q385,76 399,76 H521 Q535,76 535,90 V647 H385 Z"/>
    <path class="back-panel" role="img" aria-label="Terracotta panel with faint tonal pattern"
      fill="var(--terracotta)" d="M682,266 H830 V821 Q830,834 817,834 H695 Q682,834 682,821 Z"/>
    <rect fill="var(--paper)" x="240" y="284" width="143" height="344"/>
    <rect fill="var(--paper)" x="538" y="284" width="144" height="344"/>
    <rect fill="var(--paper)" x="911" y="305" width="101" height="119"/>
    <path class="label-band" role="img" aria-label="Terracotta label band with tonal pattern"
      fill="var(--terracotta)" d="M911,424 H1012 V607 Q1012,619 1000,619 H923 Q911,619 911,607 Z"/>
  </svg>

  <!-- top tuck flap -->
  <div class="abs center brand" style="left:385px; top:146px; width:150px;">dovrenta</div>

  <!-- front panel -->
  <div class="abs center brand" style="left:385px; top:381px; width:150px;">dovrenta</div>
  <div class="abs center product-name" style="left:385px; top:459px; width:150px;">SKIN<br>ELIXIR SERUM</div>
  <div class="abs center uses" style="left:385px; top:505px; width:150px;">FACE &nbsp;|&nbsp; NECK &nbsp;|&nbsp; EYE</div>
  <div class="abs center claims" style="left:385px; top:532px; width:150px;">completely natural, super<br>concentrated, multi use</div>
  <div class="abs center volume" style="left:385px; top:573px; width:150px;">Natural Serum<br><b>30ml</b></div>

  <!-- left side copy -->
  <div class="abs copy" style="left:250px; top:309px;">
    <p>Lorem Ipsum is simply dummy text of the printing and typesetting industry. Lorem Ipsum has been the industry's standard dummy text ever since the 1500s</p>
    <p class="strong gap-1">Lorem Ipsum is simply dummy text of the printing and typesetting industry.</p>
    <p class="gap-2">Lorem Ipsum is simply dummy text of the printing and typesetting industry. Lorem Ipsum has been the industry's standard dummy text ever since the 1500s</p>
    <p class="strong gap-3">Lorem Ipsum is simply dummy text of the printing</p>
    <p class="strong gap-4">dummy text of the printing</p>
  </div>

  <!-- right side copy -->
  <div class="abs copy" style="left:548px; top:309px;">
    <p>Lorem Ipsum is simply dummy text of the printing and typesetting industry. Lorem Ipsum has been the industry's standard dummy text ever since the 1500s</p>
    <p class="strong gap-1">Lorem Ipsum is simply dummy text of the printing and typesetting industry.</p>
    <p class="gap-2">Lorem Ipsum is simply dummy text of the printing and typesetting industry. Lorem Ipsum has been the industry's standard dummy text ever since the 1500s</p>
    <p class="strong gap-3">Lorem Ipsum is simply dummy text of the printing</p>
    <p class="strong gap-4">dummy text of the printing</p>
  </div>

  <!-- back panel -->
  <div class="abs center brand" style="left:682px; top:426px; width:148px;">dovrenta</div>

  <!-- bottle label -->
  <div class="label">
    <div class="abs center brand" style="left:911px; top:457px; width:101px;">dovrenta</div>
    <div class="abs center product-name" style="left:911px; top:507px; width:101px;">SKIN<br>ELIXIR SERUM</div>
    <div class="abs center uses" style="left:911px; top:544px; width:101px;">FACE &nbsp;|&nbsp; NECK &nbsp;|&nbsp; EYE</div>
    <div class="abs center claims" style="left:911px; top:563px; width:101px;">completely natural, super<br>concentrated, multi use</div>
    <div class="abs center volume" style="left:911px; top:587px; width:101px;">Natural Serum<br><b>30ml</b></div>
  </div>
</main>
</body>
</html>
```